KRT-VB 2018 Recycling Rate Report

We need a design for our 2018 Recycling Rate Report on Expanded Polystyrene. We want to move from a larger booklet style to a two page document. The report from last year - which was done as a booklet - is attached to provide an example of our style and design.The primary items that must be included (but not limited to) the information on pages 3, 5 & 7. The graphs must include room for 2018 data.To view our typical company design/style please see our website at www.kortavale.org. Our primary RGB colors are: (187,140,9); (94,47,29); (94,138,164); and (164,167,15). Secondary RGB colors are (249,162,28) and (218,210,208). Our title/header font is DIN Next LT Pro and our copy font is Calibri 10.5 pt. We can deviate from the font specification if beneficial and welcome interesting text treatments and typography.

Target Market(s)

Recycling facilities & general public.

Font styles to use
Sans Serif

Requirements
Must have
• Information presentation must be clean and easy to reference.

```html
<!DOCTYPE html>
<html lang="en">
<head>
<meta charset="utf-8">
<title>KRT-VB 2018 Recycling Rate Report</title>
<link href="https://fonts.googleapis.com/css2?family=Montserrat:wght@700;800&family=Questrial&family=Carlito:wght@400;700&display=swap" rel="stylesheet">
<style>
  :root{
    --gold:#bb8c09;
    --brown:#5e2f1d;
    --blue:#5e8aa4;
    --olive:#a4a70f;
    --orange:#f9a21c;
    --stone:#dad2d0;
    --ink:#1c1c1c;
    --grid:#dcdcdc;
  }
  *{margin:0;padding:0;box-sizing:border-box}
  html,body{width:927px;height:1200px;overflow:hidden;background:var(--stone)}
  body{position:relative;font-family:"Carlito",Calibri,sans-serif;color:var(--ink)}
  .top-bar{position:absolute;left:0;top:0;width:927px;height:36px;background:var(--brown);color:#fff}
  .edition{position:absolute;right:22px;top:5px;display:flex;align-items:center;gap:4px;font-family:"Questrial",sans-serif}
  .edition-year{font-size:24px;line-height:1}
  .edition-name{font-size:10px;line-height:1.05;letter-spacing:.2px}
  .masthead{position:absolute;left:0;top:36px;width:927px;height:109px}
  .masthead-kicker{position:absolute;left:34px;top:18px;width:197px;text-align:right;font-family:"Questrial",sans-serif;color:var(--gold);font-size:39px;line-height:39px;letter-spacing:1px}
  .masthead-title{position:absolute;left:258px;top:14px;font-family:"Montserrat",sans-serif;font-weight:700;color:var(--gold);font-size:76px;line-height:80px;letter-spacing:1px;white-space:nowrap}
  .panel{position:absolute;top:145px;height:366px}
  .panel-methodology{left:0;width:463px;background:var(--gold);color:#fff;padding:20px 24px 0 28px}
  .panel-collection{left:464px;width:463px;background:var(--blue);color:var(--ink);padding:10px 14px 0 27px}
  .panel h2{font-family:"Questrial",sans-serif;font-weight:400;letter-spacing:1px}
  .panel-methodology h2{font-size:34px;line-height:1;margin:13px 0 18px}
  .panel-collection h2{font-size:34px;line-height:32px;margin:8px 0 4px}
  .panel p{font-size:14.2px;line-height:19.7px}
  .panel p + p{margin-top:19.7px}
  .photo{position:absolute;top:518px;width:192px;height:133px}
  .photo-industrial{left:23px;background:linear-gradient(135deg,#5a5d62 0%,#c9ccd0 45%,#f2f2f2 70%,#8a8d92 100%)}
  .photo-consumer{left:257px;background:linear-gradient(160deg,#2b2d30 0%,#6f7378 40%,#e8e8e8 62%,#8ea8c0 85%,#3a3c3f 100%)}
  .stat{position:absolute;top:652px;width:240px;text-align:center}
  .stat-industrial{left:0}
  .stat-consumer{left:233px}
  .stat-label{font-family:"Questrial",sans-serif;font-size:20.5px;line-height:24px}
  .stat-unit{font-family:"Questrial",sans-serif;font-size:10px;line-height:12px}
  .stat-value{font-family:"Montserrat",sans-serif;font-weight:800;font-size:52px;line-height:56px}
  .stat-industrial .stat-value{color:var(--orange)}
  .stat-consumer .stat-value{color:var(--olive)}
  .summary{position:absolute;left:486px;top:535px;width:400px;font-size:14.2px;line-height:19.2px}
  .chart-title{position:absolute;left:0;top:756px;width:927px;text-align:center;font-family:"Questrial",sans-serif;font-size:22px;letter-spacing:.5px}
  .chart{position:absolute;left:17px;top:791px;width:885px;height:369px;background:#fff}
  .chart svg{display:block;width:885px;height:369px}
  .axis-num{font-family:"Questrial",sans-serif;font-size:17px;fill:var(--olive)}
  .year{font-family:"Questrial",sans-serif;font-size:17px;fill:var(--ink)}
  .val{font-family:"Questrial",sans-serif;font-size:17px;fill:var(--ink)}
  .axis-title{font-family:"Questrial",sans-serif;font-size:17px;fill:#a8a8a8}
  .bottom-bar{position:absolute;left:0;top:1168px;width:927px;height:32px;background:var(--gold)}
  .bottom-bar::before{content:"";position:absolute;left:0;top:0;width:763px;height:32px;background:var(--blue)}
</style>
</head>
<body>
  <header class="top-bar">
    <div class="edition"><span class="edition-year">2018</span><span class="edition-name">EPS RECYCLING<br>RATE REPORT</span></div>
  </header>

  <section class="masthead">
    <div class="masthead-kicker">TAKE A<br>LOOK AT</div>
    <h1 class="masthead-title">EPS RECYCLING</h1>
  </section>

  <section class="panel panel-methodology">
    <h2>METHODOLOGY</h2>
    <p>The 2017 Expanded Polystyrene Recycling Rate Study was conducted by the Kortavale Board to gather data to reflect both post-consumer and post-industrial recycling activity. The 2017 results are based on data received from 55 EPS manufacturers and independent recyclers in the U.S.</p>
    <p>Participation in the EPS recycling survey is voluntary and the reported data is based on the responses received. Many companies have limited resources to put towards participation in the survey, and some companies may choose not to respond due to their confidentiality policies. Therefore, because there is not 100 percent participation, the presented totals represent the minimum amount of EPS recovered for recycling.</p>
  </section>

  <section class="panel panel-collection">
    <h2>COLLECTION OPTIONS<br>&amp; RESOURCES</h2>
    <p>Not everything can be recycled all the time. In order for materials to be recycled, stable markets must exist and there must be a demand for the end products. Each community has its own guidelines for which plastics are accepted, and these can vary widely. Some locations also offer consumer dropoff access. To find out if EPS recycling is available in your area, visit www.kortavale.org.</p>
    <p>For consumers that do not have access to a local drop-off center, the KRT-VB sponsors a National Mail-Back Program intended for smaller quantities of EPS which can be mailed via NPost or ParcelLine to more than 20 locations nationwide. Full instructions and a list of Mail-Back locations are available on the KRT-VB website.</p>
  </section>

  <div class="photo photo-industrial" role="img" aria-label="Worker sorting large white EPS blocks at an industrial recycling line"></div>
  <div class="photo photo-consumer" role="img" aria-label="Person dropping a sheet of EPS foam into a collection bin"></div>

  <div class="stat stat-industrial">
    <div class="stat-label">Post-Industrial</div>
    <div class="stat-unit">(millions of pounds)</div>
    <div class="stat-value">39.0</div>
  </div>
  <div class="stat stat-consumer">
    <div class="stat-label">Post-Consumer</div>
    <div class="stat-unit">(millions of pounds)</div>
    <div class="stat-value">25.9</div>
  </div>

  <p class="summary">The 25-year baseline shows incremental gains with more than 23 million pounds of EPS recycled annually on average. Like all commodity markets, the EPS recycling market is cyclical. The 2017 results reflect a decrease from 2016 due to the new landscape for recycling commodities and chaning international markets, especially in China.</p>

  <h3 class="chart-title">Post-Consumer EPS Recycling 1990-2017</h3>

  <figure class="chart">
    <svg viewBox="0 0 1217 507" xmlns="http://www.w3.org/2000/svg">
      <g stroke="var(--grid)" stroke-width="1.2">
        <line x1="174" y1="16" x2="174" y2="472"/><line x1="246" y1="16" x2="246" y2="472"/>
        <line x1="319" y1="16" x2="319" y2="472"/><line x1="392" y1="16" x2="392" y2="472"/>
        <line x1="464" y1="16" x2="464" y2="472"/><line x1="536" y1="16" x2="536" y2="472"/>
        <line x1="609" y1="16" x2="609" y2="472"/><line x1="681" y1="16" x2="681" y2="472"/>
        <line x1="754" y1="16" x2="754" y2="472"/><line x1="826" y1="16" x2="826" y2="472"/>
        <line x1="899" y1="16" x2="899" y2="472"/><line x1="971" y1="16" x2="971" y2="472"/>
        <line x1="1044" y1="16" x2="1044" y2="472"/><line x1="1116" y1="16" x2="1116" y2="472"/>
        <line x1="1188" y1="16" x2="1188" y2="472"/>
      </g>
      <line x1="101" y1="16" x2="101" y2="472" stroke="#bdbdbd" stroke-width="1.2"/>
      <g stroke="#bdbdbd" stroke-width="1.2">
        <line x1="93" y1="455" x2="101" y2="455"/><line x1="93" y1="394.3" x2="101" y2="394.3"/>
        <line x1="93" y1="333.6" x2="101" y2="333.6"/><line x1="93" y1="272.9" x2="101" y2="272.9"/>
        <line x1="93" y1="212.2" x2="101" y2="212.2"/><line x1="93" y1="151.5" x2="101" y2="151.5"/>
        <line x1="93" y1="90.8" x2="101" y2="90.8"/><line x1="93" y1="30.1" x2="101" y2="30.1"/>
      </g>
      <g class="axis-num" text-anchor="end">
        <text x="86" y="461">0</text><text x="86" y="400">10</text><text x="86" y="339">20</text>
        <text x="86" y="279">30</text><text x="86" y="218">40</text><text x="86" y="157">50</text>
        <text x="86" y="97">60</text><text x="86" y="36">70</text>
      </g>
      <text class="axis-title" transform="translate(36 247) rotate(-90)" text-anchor="middle">Millions of Pounds Recycled</text>
      <g class="year" text-anchor="middle">
        <text x="133" y="478">1990</text><text x="206" y="478">1992</text><text x="279" y="478">1994</text>
        <text x="352" y="478">1996</text><text x="425" y="478">1998</text><text x="498" y="478">2000</text>
        <text x="571" y="478">2002</text><text x="644" y="478">2004</text><text x="717" y="478">2006</text>
        <text x="790" y="478">2008</text><text x="862" y="478">2010</text><text x="935" y="478">2012</text>
        <text x="1008" y="478">2016</text><text x="1079" y="478">2017</text><text x="1155" y="478">2018</text>
      </g>
      <polyline fill="none" stroke="#9a9a2e" stroke-width="2.2"
        points="136,437 211,329 285,308 354,318 429,344 501,304 572,296 644,303 717,261 788,251 863,230 934,232 1013,73 1079,298"/>
      <g fill="#9a9a2e">
        <circle cx="136" cy="437" r="6.5"/><circle cx="211" cy="329" r="6.5"/><circle cx="285" cy="308" r="6.5"/>
        <circle cx="354" cy="318" r="6.5"/><circle cx="429" cy="344" r="6.5"/><circle cx="501" cy="304" r="6.5"/>
        <circle cx="572" cy="296" r="6.5"/><circle cx="644" cy="303" r="6.5"/><circle cx="717" cy="261" r="6.5"/>
        <circle cx="788" cy="251" r="6.5"/><circle cx="863" cy="230" r="6.5"/><circle cx="934" cy="232" r="6.5"/>
        <circle cx="1013" cy="73" r="6.5"/><circle cx="1079" cy="298" r="6.5"/>
      </g>
      <g class="val" text-anchor="middle">
        <text x="136" y="416">3.0</text><text x="209" y="308">20.8</text><text x="285" y="287">24.2</text>
        <text x="354" y="298">22.5</text><text x="428" y="324">18.2</text><text x="500" y="283">24.9</text>
        <text x="572" y="276">26.2</text><text x="644" y="282">25.0</text><text x="717" y="239">32.0</text>
        <text x="788" y="229">33.6</text><text x="863" y="209">37.1</text><text x="927" y="211">36.7</text>
        <text x="1013" y="52">63.0</text><text x="1079" y="321">25.9</text>
      </g>
    </svg>
  </figure>

  <footer class="bottom-bar"></footer>
</body>
</html>
```